Webdesign für Automotive Engineering Webpage
Zielgruppe
Automotive Engineering - Main focus is Software Development & Embedded systems for the Automotive industry.
Like as HMI, ADAS, ECU
Aufgabenstellung
See Logo (PDF), example --> https://www.trelvona.com/de/de (competetor)

```html
<!DOCTYPE html>
<html lang="de">
<head>
<meta charset="utf-8">
<title>Novaris – Automotive Engineering</title>
<link rel="stylesheet" href="https://fonts.googleapis.com/css2?family=Audiowide&family=Questrial&display=swap">
<style>
:root{
  --navy:#0d2d68;
  --navy-deep:#0a2457;
  --red:#e4252b;
  --white:#ffffff;
  --ink:#0d2d68;
  --muted:#f3f4f6;
}
*{box-sizing:border-box;margin:0;padding:0}
html,body{width:1200px;height:3442px;overflow:hidden;background:var(--white)}
body{position:relative;font-family:"Questrial",sans-serif;color:var(--ink)}
.abs{position:absolute}
.display{font-family:"Audiowide",sans-serif;font-weight:400;line-height:1.15}
.red{color:var(--red)}
.white{color:var(--white)}

/* header */
.header{left:0;top:0;width:1200px;height:103px;background:var(--white)}
.menu-btn{left:0;top:0;width:55px;height:103px;background:var(--red)}
.menu-btn span{position:absolute;left:17px;width:22px;height:2px;background:var(--white)}
.brand{left:500px;top:46px;width:200px;text-align:center}
.brand-name{font-family:"Audiowide",sans-serif;font-size:26px;color:var(--red);letter-spacing:1px}
.brand-tag{font-size:7px;color:var(--red);margin-top:2px}
.brand-dot{left:595px;top:24px;width:10px;height:10px;border-radius:50%;background:var(--navy)}

/* sidebar */
.sidebar{left:0;top:103px;width:55px;height:539px;background:var(--navy)}
.sidebar svg{position:absolute;left:19px}
.side-brand{left:-20px;top:450px;width:95px;transform:rotate(-90deg);font-family:"Audiowide",sans-serif;font-size:20px;color:var(--white);text-align:center}

/* hero */
.hero{left:55px;top:103px;width:1145px;height:539px;background:radial-gradient(ellipse at 55% 55%,#2f9be0 0%,#1a4e8a 35%,#14284d 70%,#0f1a33 100%)}
.scroll-mouse{left:590px;top:580px;width:19px;height:29px;border:2px solid var(--white);border-radius:10px}
.scroll-mouse::after{content:"";position:absolute;left:6px;top:5px;width:3px;height:6px;border-radius:2px;background:var(--white)}

/* business areas */
.area-title{left:98px;top:870px;font-size:28px}
.card{width:235px}
.card .photo{height:210px}
.card .label{height:44px;padding:0 21px;display:flex;align-items:center;font-family:"Audiowide",sans-serif;font-size:13px;color:var(--white);background:var(--navy)}
.card .label.is-active{background:var(--red)}

/* engineering band */
.band{left:0;width:1200px;background:var(--navy)}
.eng-title{left:98px;top:1148px;font-size:28px}
.eng-copy{left:98px;top:1238px;width:265px;font-size:12px;line-height:19px;color:var(--white)}
.eng-copy p{margin-bottom:21px}
.tile{width:235px}
.tile .photo{height:181px}
.tile .label{height:43px;padding:0 21px;display:flex;align-items:center;font-family:"Audiowide",sans-serif;font-size:11px;line-height:12px;color:var(--navy);background:var(--white)}
.tile .label.is-active{background:var(--red);color:var(--white)}

/* split text sections */
.split-title{left:98px;font-size:28px}
.rule{left:389px;width:3px;background:var(--red)}
.split-copy{left:433px;width:712px;font-size:12px;line-height:19px}
.split-copy p{margin-bottom:19px}

/* services */
.services{left:0;top:2374px;width:1200px;height:568px;background:linear-gradient(90deg,#ffffff 0%,#f7f7f8 50%,#eceef1 100%)}
.car{left:555px;top:2440px;width:645px;height:502px;background:radial-gradient(ellipse at 55% 55%,#dfe1e4 0%,#b9bcc2 40%,#4a4d53 75%,rgba(236,238,241,0) 100%)}
.svc-title{left:98px;font-family:"Audiowide",sans-serif;font-size:17px;color:var(--red)}
.svc-sub{left:98px;font-size:12px;color:var(--navy)}

/* contact */
.contact-title{left:98px;top:3010px;font-size:28px;line-height:33px}
.contact-copy{left:98px;top:3176px;width:400px;font-size:12px;line-height:19px;color:var(--white)}
.field{width:284px;height:36px;background:var(--white);font-size:11px;color:#555;padding:0 15px;display:flex;align-items:center}
.field b{color:var(--red);font-weight:400;margin-left:3px}
.message{left:861px;top:3015px;width:284px;height:148px;align-items:flex-start;padding-top:13px}
.submit{left:861px;top:3184px;width:284px;height:36px;background:var(--red);color:var(--white);font-size:10px;letter-spacing:1px;display:flex;align-items:center;justify-content:center;font-weight:700;box-shadow:0 3px 0 #a8181c}

/* footer */
.foot-brand{left:98px;top:3346px;font-family:"Audiowide",sans-serif;font-size:28px;color:var(--red)}
.foot-tag{left:98px;top:3384px;font-size:7px;color:var(--red)}
.foot-col{top:3340px;font-size:10.5px;line-height:14px;color:#333}
.foot-col h4{font-size:10.5px;color:var(--red);margin-bottom:10px;font-weight:700}
.social{top:3360px;width:18px;height:18px;border-radius:50%;border:2px solid var(--navy)}
.social.is-red{border-color:var(--red)}
</style>
</head>
<body>

<header class="abs header"></header>
<div class="abs menu-btn"><span style="top:44px"></span><span style="top:51px"></span><span style="top:58px"></span></div>
<div class="abs brand-dot"></div>
<div class="abs brand"><div class="brand-name">NOVARIS</div><div class="brand-tag">Automotive Engineering &amp; Recruiting</div></div>

<nav class="abs sidebar">
  <svg style="top:60px" width="16" height="16" viewBox="0 0 16 16" fill="none" stroke="#fff" stroke-width="1.4"><circle cx="7" cy="7" r="4.5"/><path d="M10.5 10.5l3.5 3.5"/></svg>
  <svg style="top:100px" width="16" height="16" viewBox="0 0 16 16" fill="none" stroke="#fff" stroke-width="1.2"><circle cx="8" cy="8" r="6"/><ellipse cx="8" cy="8" rx="2.6" ry="6"/><path d="M2 8h12"/></svg>
  <svg style="top:140px" width="16" height="16" viewBox="0 0 16 16" fill="none" stroke="#fff" stroke-width="1.3"><path d="M3 2.5l3 .5 1 3-1.5 1.2a8 8 0 0 0 3.3 3.3L10 9l3 1 .5 3-2 1A11 11 0 0 1 2 4.5z"/></svg>
  <svg style="top:180px" width="16" height="16" viewBox="0 0 16 16" fill="none" stroke="#fff" stroke-width="1.3"><circle cx="8" cy="7.5" r="5.5"/><path d="M4.5 12l-1.5 2.5 3-1.3"/></svg>
  <div class="abs side-brand">NOVARIS</div>
</nav>

<section class="abs hero" role="img" aria-label="Ingenieurin mit Tablet vor einer leuchtend blauen Drahtgitter-Simulation eines Sportwagens in einer Halle"></section>
<div class="abs scroll-mouse"></div>

<!-- Geschäftsbereiche -->
<h2 class="abs display area-title">Unsere<br><span class="red">Geschäftsbereiche</span></h2>
<div class="abs card" style="left:433px;top:724px">
  <div class="photo" role="img" aria-label="Digitale Fahrzeugvisualisierung über einem Tablet" style="background:linear-gradient(160deg,#d7e6ef,#7fb4d6 60%,#4d7fa3)"></div>
  <div class="label is-active">Full Service Engineering</div>
</div>
<div class="abs card" style="left:671px;top:724px">
  <div class="photo" role="img" aria-label="Mechaniker mit Tablet in einer Werkstatt" style="background:linear-gradient(160deg,#e69a3a,#7a6a5a 50%,#2b3d6a)"></div>
  <div class="label">Premium Recruiting</div>
</div>
<div class="abs card" style="left:910px;top:724px">
  <div class="photo" role="img" aria-label="Rad und Fahrwerk eines Fahrzeugchassis" style="background:linear-gradient(160deg,#d4d8dd,#8f969e 55%,#3b4048)"></div>
  <div class="label">Temping</div>
</div>

<!-- Individuelles Full Service Engineering -->
<section class="abs band" style="top:1058px;height:592px"></section>
<h2 class="abs display white eng-title">Individuelles <span class="red">Full<br>Service Engineering</span></h2>
<div class="abs eng-copy">
  <p>Neben der Entlastung bei Bedarfsspitzen und der Direktvermittlung von Vakanzen übernehmen wir auch Ihre Projekte komplett als Fremdleistung. Sie übergeben uns Ihre Aufgaben, wir liefern Ihnen das Ergebnis – pünktlich und qualitativ hochwertig!</p>
  <p>Unsere Teams beherrschen unter anderem die Sparten</p>
  <p>Bei uns finden Sie die Ressourcen, die Ihnen fehlen</p>
  <p>Unsere Arbeit ist in allen Details darauf ausgerichtet, dass Sie Ihre Projekte so schnell wie möglich zum Erfolg führen können.</p>
</div>
<div class="abs tile" style="left:433px;top:1116px">
  <div class="photo" role="img" aria-label="Fahrzeugcockpit mit digitalen Anzeigen auf der Straße" style="background:linear-gradient(170deg,#8fb7c9,#3f6e8c 50%,#1d2f48)"></div>
  <div class="label is-active">E-Mobilität / Elektrifizierung</div>
</div>
<div class="abs tile" style="left:671px;top:1116px">
  <div class="photo" role="img" aria-label="Innenraum eines autonomen Fahrzeugs mit leuchtendem Display" style="background:linear-gradient(170deg,#4aa2d8,#1b4e86 55%,#0b1d3c)"></div>
  <div class="label">Autonomes Fahren</div>
</div>
<div class="abs tile" style="left:910px;top:1116px">
  <div class="photo" role="img" aria-label="Cockpit mit Assistenzsystem-Anzeigen" style="background:linear-gradient(170deg,#5ab2e6,#235d98 55%,#0c2246)"></div>
  <div class="label">Fahrassistenzsysteme, ADAS</div>
</div>
<div class="abs tile" style="left:433px;top:1346px">
  <div class="photo" role="img" aria-label="Hand bedient ein holografisches Fahrzeugmenü" style="background:linear-gradient(170deg,#c7dbe6,#6f98b3 55%,#33536e)"></div>
  <div class="label">Prototypen / Testing</div>
</div>
<div class="abs tile" style="left:671px;top:1346px">
  <div class="photo" role="img" aria-label="Leuchtendes Fahrzeugmodell über einer Hand" style="background:linear-gradient(170deg,#2f7fc2,#154a86 55%,#08193a)"></div>
  <div class="label">Prozessoptimierung in der Produktentwicklung</div>
</div>
<div class="abs tile" style="left:910px;top:1346px">
  <div class="photo" role="img" aria-label="Fahrzeughologramm über geöffneten Händen" style="background:linear-gradient(170deg,#d3e3ef,#8ab3d3 55%,#5a7fa0)"></div>
  <div class="label">Projektmanagement</div>
</div>

<!-- Originate -->
<h2 class="abs display split-title" style="top:1752px">Originate<br><span class="red">in Engineering</span></h2>
<div class="abs rule" style="top:1737px;height:243px"></div>
<div class="abs split-copy" style="top:1752px">
  <p>Novaris Recruitment vereint in sich 25 Jahre Branchen- und Projekterfahrung vom Freelance Ingenieur bis zum Task Force Manager in den Branchen Automotive, Schienenfahrzeuge, Luft- und Raumfahrt, Rüstung und Informationstechnologie.</p>
  <p>Firmengründer und Geschäftsführer Jonas Weller kennt die Industrie seit über zwei Jahrzehnten, in denen er in Positionen als IT Entwicklungsingenieur, Experte für Geodaten und rund um das Thema autonomes Fahren und Fahrassistenzsysteme, bis zum CIO und Task Force Manager bei fast allen wichtigen OEMs und Tier1s des Automotive Sektors und anderer Schlüsselindustrien Erfahrungen sammeln konnte.</p>
  <p>Wie der Firmengründer, so verfügen auch alle maßgeblichen Mitarbeiter bei Novaris Recruitment über diese Double Qualification – wir sprechen Ihre Sprache und wissen, wo Ihr Bedarf liegt, kennen Ihre Abläufe und Prozesse, sind aus eigener Erfahrung heraus im Geschäft.</p>
</div>

<!-- Erfolg -->
<section class="abs band" style="top:2067px;height:307px"></section>
<h2 class="abs display white split-title" style="top:2155px"><span class="red">Erfolg</span> wird<br>aus Wissen<br>generiert</h2>
<div class="abs rule" style="top:2145px;height:150px"></div>
<div class="abs split-copy white" style="top:2158px">
  <p>Diese mehr als zwei Jahrzehnte in der Automotive- und anderen Schlüsselindustrien hinterlassen auch ihre Spuren in Form eines großen, etablierten Netzwerks: vom Testfahrer bis zum C-Level Manager kennen wir zahlreiche Professionals aus der Branche, und haben mit Ihnen bereits in unterschiedlichsten Projekten zusammengearbeitet.</p>
  <p>Deshalb recherchieren wir nicht nach dem Papier und abstrakten Kriterien für irgendeinen Personalbedarf, sondern wissen in den meisten Fällen konkret, welche Personen für Ihr Projekt geeignet sind, um es schnell zum Erfolg zu führen!</p>
</div>

<!-- Services -->
<section class="abs services"></section>
<div class="abs car" role="img" aria-label="Weißer Sportwagen in der Seitenansicht von hinten"></div>
<svg class="abs" style="left:98px;top:2448px" width="46" height="44" viewBox="0 0 46 44" fill="none" stroke="#e4252b" stroke-width="3"><circle cx="23" cy="7" r="5" fill="#e4252b"/><circle cx="7" cy="34" r="5" fill="#e4252b"/><circle cx="39" cy="34" r="5" fill="#e4252b"/><path d="M14 10A17 17 0 0 0 6 26M32 10a17 17 0 0 1 8 16M14 40a17 17 0 0 0 18 0"/></svg>
<div class="abs svc-title" style="top:2515px">Full Service Engineering:</div>
<div class="abs svc-sub" style="top:2539px">Übernahme kompletter R&amp;D Projekte als Fremdleistung</div>
<svg class="abs" style="left:98px;top:2604px" width="86" height="46" viewBox="0 0 86 46" fill="#e4252b"><circle cx="11" cy="6" r="5"/><path d="M3 14h16v16h-3v16h-10v-16h-3z"/><circle cx="33" cy="6" r="5"/><path d="M25 14h16v16h-3v16h-10v-16h-3z"/><circle cx="55" cy="6" r="5"/><path d="M47 14h16v16h-3v16h-10v-16h-3z"/><circle cx="77" cy="6" r="5"/><path d="M69 14h16v16h-3v16h-10v-16h-3z"/></svg>
<div class="abs svc-title" style="top:2671px">Premium Recruiting:</div>
<div class="abs svc-sub" style="top:2695px">Vermittlung bis hin zum Onboarding von Freelancern und Festangestellten</div>
<svg class="abs" style="left:98px;top:2755px" width="46" height="44" viewBox="0 0 46 44" fill="none" stroke="#e4252b" stroke-width="2.5"><rect x="6" y="3" width="28" height="32" rx="2"/><path d="M11 11h18M11 17h18M11 23h10"/><circle cx="33" cy="32" r="9" fill="#fff"/><circle cx="33" cy="32" r="4" fill="#e4252b"/></svg>
<div class="abs svc-title" style="top:2819px">Arbeitnehmerüberlassung:</div>
<div class="abs svc-sub" style="top:2843px">Automotive R&amp;D Experten und Ingenieure in Zeitarbeit</div>

<!-- Contact -->
<section class="abs band" style="top:2942px;height:355px"></section>
<h2 class="abs display white contact-title">Sie suchen Spezialisten<br>für eine bestimmte Aufgabe,<br>oder möchten mit uns in<br>Kontakt treten?</h2>
<p class="abs contact-copy">Senden Sie uns zum Beispiel Ihre Anforderungen und wir kommen mit passenden Profilen auf Sie zu, oder nehmen Sie einfach mit uns Kontakt auf und erfahren was wir für Sie tun können.</p>
<div class="abs field" style="left:558px;top:3015px">Name<b>*</b></div>
<div class="abs field" style="left:558px;top:3072px">PflichtfeldE-Mail<b>*</b></div>
<div class="abs field" style="left:558px;top:3128px">Telefonnummer</div>
<div class="abs field" style="left:558px;top:3184px">PflichtfeldOrt/PLZ<b>*</b></div>
<div class="abs field message">Ihre Nachricht an uns</div>
<div class="abs submit">ANFRAGE ABSENDEN</div>

<!-- Footer -->
<div class="abs foot-brand">NOVARIS</div>
<div class="abs foot-tag">Automotive Engineering &amp; Recruiting</div>
<div class="abs foot-col" style="left:330px"><h4>Adresse</h4>Novaris GmbH<br>Lindenstraße 12<br>D - 34100 Talbach OT Ellingen</div>
<div class="abs foot-col" style="left:592px"><h4>Kontakt</h4>T: +49 (0)5100 - 123 45 67<br>E: kontakt@novaris-recruitment.de</div>
<div class="abs foot-col" style="left:842px"><h4>Links</h4>Impressum<br>Datenschutz<br>Registrieren</div>
<div class="abs social" style="left:1014px"></div>
<div class="abs social is-red" style="left:1050px"></div>
<div class="abs social" style="left:1088px"></div>
<div class="abs social" style="left:1126px"></div>

</body>
</html>
```